Valmo Sàrl - Business Card

VALMO Sàrl operates in the sector Services for banks and credit institutions. It is a B2B which connects companies. The main colors should be Blue and Black. The logo and look of the card should be simple, professional, conservative and reflect Connecting People.

Target Market(s)

Financial professionals and institutions

Industry/Entity Type

Finance

Contact Information for Business Card

Chemin des Vergers 9
1026 Denges

Logo Text

Connecting dots

Font styles to use
Serif
Sans Serif

Colors
0355a3
3176b5
85acd3
cfdeed

Requirements
Should not have
• Multiple colors

```html
<!DOCTYPE html>
<html lang="en">
<head>
<meta charset="utf-8">
<title>Valmo Sàrl – Business Card</title>
<link rel="stylesheet" href="https://fonts.googleapis.com/css2?family=Quicksand:wght@400;500;700&display=swap">
<style>
  :root {
    --bg: #2b2b2d;
    --card: #151516;
    --card-edge: #0c0c0d;
    --blue: #0355a3;
    --blue-mid: #3176b5;
    --blue-light: #85acd3;
    --grey-text: #8a8a8e;
    --grey-soft: #5e5e62;
  }
  * { margin: 0; padding: 0; box-sizing: border-box; }
  html, body { width: 1200px; height: 716px; overflow: hidden; }
  body {
    background: var(--bg);
    font-family: "Quicksand", sans-serif;
    position: relative;
  }
  .card {
    position: absolute;
    width: 500px;
    height: 286px;
    background: var(--card);
    border-radius: 18px;
    box-shadow: 0 6px 0 var(--card-edge), 0 18px 40px rgba(0,0,0,.45);
  }
  .card--front { left: 70px; top: 50px; }
  .card--back { left: 630px; top: 270px; }

  .brand {
    display: flex;
    align-items: center;
    gap: 12px;
    color: var(--blue-mid);
    font-weight: 400;
    white-space: nowrap;
  }
  .brand__mark {
    width: 14px; height: 14px;
    border-radius: 50%;
    background: var(--blue);
    flex: none;
  }
  .card--front .brand {
    position: absolute; left: 50%; top: 50%;
    transform: translate(-50%, -50%);
    font-size: 42px;
  }

  .card--back .brand {
    position: absolute; left: 36px; top: 50%;
    transform: translateY(-50%);
    font-size: 30px;
  }
  .card--back .brand__mark { width: 11px; height: 11px; }
  .divider {
    position: absolute; left: 262px; top: 58px;
    width: 1px; height: 170px;
    background: var(--blue);
  }
  .contact {
    position: absolute; left: 284px; top: 66px;
    color: var(--grey-text);
  }
  .contact__name { font-size: 17px; font-weight: 700; color: #b8b8bc; }
  .contact__title { font-size: 11px; color: var(--blue-mid); margin-top: 2px; }
  .contact__list { list-style: none; margin-top: 22px; }
  .contact__item {
    display: flex; align-items: center; gap: 10px;
    font-size: 13px; font-weight: 500; margin-bottom: 11px;
  }
  .contact__item svg { width: 12px; height: 12px; flex: none; }

  .showcase-logo {
    position: absolute; left: 56px; top: 585px;
    font-size: 50px;
  }
  .showcase-logo .brand__mark { width: 18px; height: 18px; }
</style>
</head>
<body>
  <section class="card card--front" aria-label="Card front">
    <div class="brand"><span class="brand__mark"></span>Valmo Sàrl</div>
  </section>

  <section class="card card--back" aria-label="Card back">
    <div class="brand"><span class="brand__mark"></span>Valmo Sàrl</div>
    <div class="divider"></div>
    <div class="contact">
      <p class="contact__name">Your Name</p>
      <p class="contact__title">Job Title</p>
      <ul class="contact__list">
        <li class="contact__item">
          <svg viewBox="0 0 12 12"><path d="M3 1h2l1 3-1.5 1a6 6 0 0 0 2.5 2.5L8 6l3 1v2c0 1-1 2-2 2A8 8 0 0 1 1 3c0-1 1-2 2-2z" fill="var(--blue-light)"/></svg>
          000 000 0000
        </li>
        <li class="contact__item">
          <svg viewBox="0 0 12 12"><rect x="1" y="2.5" width="10" height="7" rx="1" fill="var(--blue-light)"/><path d="M1.5 3 6 6.5 10.5 3" stroke="var(--card)" fill="none"/></svg>
          youremail@xyz.com
        </li>
        <li class="contact__item">
          <svg viewBox="0 0 12 12" fill="none" stroke="var(--blue-light)"><circle cx="6" cy="6" r="4.8"/><ellipse cx="6" cy="6" rx="2" ry="4.8"/><path d="M1.2 6h9.6"/></svg>
          www.yourwebsite.com
        </li>
      </ul>
    </div>
  </section>

  <div class="brand showcase-logo"><span class="brand__mark"></span>Valmo Sàrl</div>
</body>
</html>
```